Evergreen Roofing flyer*

I need an a5 size flyer designing to go in our local advertising magazine.We are based in the north west of England Id like key features from the website including on the flyer, possibly even reviews, what we do ect.I don't however want it too busy, simple pictures and description of service.company colours and logo. I require simple one sided business cards toonumber, web address and logowinner will receive a request to design around 5 different double sided a5 flyers too, each with all our services on one side and the other primarily for one service we have provided locally with a spacve to put the house number down.REPAIRSROOFLINEFLAT ROOFS PITCHED ROOFSSYNTHETIC ROOFSUP TO 50 YEARS WARRANTY AVAILABLERANKED THE #1 FLAT ROOFER IN THE UK OUT OF 787 REGISTERED FLAT ROOFING COMPANIESRANKED THE #10 ROOFING COMPANY IN THE UK OUT OF 1976 REGISTERED SPECIALIST ROOFING COMPANIESBOTH FOR COST, CUSTOMER SERVICE AND QUALITY WITH 5 STAR REVIEWSGUARANTEED TO FIND AND FIX A LEAKAPPROVED INSTALLERSAWARD WINNINGTIME SERVED FIXED PRICES

Target Market(s)

homeowners

Colors

Designer to choose only greyscale colors for use in the design.

Requirements
Must have
• contact details
• pictures of my work
• clear and simple

```html
<!DOCTYPE html>
<html lang="en">
<head>
<meta charset="UTF-8">
<title>Evergreen Roofing Flyer</title>
<link rel="stylesheet" href="https://fonts.googleapis.com/css2?family=Bebas+Neue&family=Montserrat:wght@400;600;700;800&family=Oswald:wght@500;700&display=swap">
<style>
  :root {
    --green: #3f8f2a;
    --green-dark: #1f5a14;
    --green-deep: #174a0f;
    --yellow: #f2c500;
    --white: #ffffff;
    --ink: #1c1c1c;
    --charcoal: #2b2b2b;
    --sky: #5b6f86;
    --brick: #9a7a5c;
  }
  * { margin: 0; padding: 0; box-sizing: border-box; }
  html, body { width: 708px; height: 1200px; overflow: hidden; background: var(--white); }
  .flyer { position: relative; width: 708px; height: 1200px; overflow: hidden; font-family: "Montserrat", sans-serif; background: var(--white); }

  .header { position: absolute; left: 0; top: 0; width: 708px; height: 160px; background: var(--white); }
  .brand { position: absolute; left: 28px; top: 48px; width: 200px; color: var(--green); font-family: "Montserrat", sans-serif; font-weight: 800; font-size: 27px; line-height: 1.05; text-transform: uppercase; }
  .warranty-panel { position: absolute; right: 0; top: 0; width: 708px; height: 160px; }
  .warranty-up { position: absolute; left: 262px; top: 62px; transform: rotate(-90deg); transform-origin: center; color: var(--white); font-family: "Oswald", sans-serif; font-weight: 700; font-size: 30px; letter-spacing: 1px; width: 80px; text-align: center; }
  .warranty-years { position: absolute; left: 330px; top: 8px; color: var(--yellow); font-family: "Bebas Neue", sans-serif; font-size: 124px; line-height: 1; letter-spacing: 1px; }
  .warranty-sub { position: absolute; left: 332px; top: 116px; color: var(--white); font-family: "Montserrat", sans-serif; font-weight: 800; font-size: 26px; letter-spacing: 0.3px; }

  .hero-photo { position: absolute; left: 0; top: 160px; width: 708px; height: 430px; background: linear-gradient(180deg, var(--sky) 0%, #8d9aa6 35%, #b9a887 62%, var(--brick) 80%, #7b6a4a 100%); }
  .divider { position: absolute; left: 0; top: 500px; width: 708px; height: 120px; }

  .lower { position: absolute; left: 0; top: 600px; width: 708px; height: 540px; }
  .work-column { position: absolute; left: 0; top: 0; width: 318px; height: 540px; background: var(--white); }
  .work-photo { position: absolute; left: 28px; width: 268px; }
  .work-photo--roof { top: -6px; height: 150px; background: linear-gradient(160deg, #c9b79a 0%, #c2552a 55%, #8e3a1c 100%); }
  .work-photo--fitter { top: 158px; height: 150px; background: linear-gradient(160deg, #2f6db3 0%, #8cb0c4 45%, #3f7c6a 75%, #2c3a33 100%); }

  .ranks { position: absolute; left: 14px; top: 330px; width: 300px; display: flex; justify-content: space-between; }
  .rank { width: 148px; text-align: center; }
  .rank-badge { display: block; margin: 0 auto 8px; width: 84px; height: 84px; }
  .rank-text { font-size: 10px; line-height: 1.35; color: var(--ink); }
  .rank-text strong { font-weight: 700; }

  .services { position: absolute; left: 318px; top: 0; width: 390px; height: 540px; background: var(--green); }
  .services-title { position: absolute; left: 32px; top: 20px; color: var(--white); font-weight: 700; font-size: 28px; text-transform: uppercase; border-bottom: 2px solid var(--yellow); padding-bottom: 2px; }
  .service-list { position: absolute; left: 32px; top: 70px; list-style: none; }
  .service-list li { display: flex; align-items: center; gap: 12px; color: var(--yellow); font-weight: 600; font-size: 25px; line-height: 42px; }
  .tick { width: 16px; height: 16px; }
  .about-title { position: absolute; left: 32px; top: 208px; color: var(--white); font-weight: 700; font-size: 28px; text-transform: uppercase; border-bottom: 2px solid var(--yellow); padding-bottom: 2px; }
  .about-text { position: absolute; left: 32px; top: 258px; width: 345px; color: var(--white); font-size: 13px; line-height: 1.4; }

  .reviews { position: absolute; left: 14px; top: 344px; width: 376px; height: 196px; background: var(--green-dark); padding: 18px 20px; color: var(--white); }
  .reviews-title { font-weight: 700; font-size: 16px; margin-bottom: 10px; }
  .review { margin-bottom: 12px; }
  .review-quote { font-size: 12px; font-style: italic; line-height: 1.35; }
  .review-foot { display: flex; justify-content: space-between; align-items: center; margin-top: 6px; }
  .review-name { font-size: 11px; font-weight: 700; text-transform: uppercase; }
  .stars { color: var(--yellow); font-size: 17px; letter-spacing: 6px; }

  .seal { position: absolute; left: 545px; top: 450px; width: 150px; height: 150px; }
  .seal-text { position: absolute; left: 545px; top: 450px; width: 150px; height: 150px; display: flex; flex-direction: column; align-items: center; justify-content: center; text-align: center; font-family: "Oswald", sans-serif; font-weight: 700; line-height: 1.1; text-transform: uppercase; }
  .seal-text .seal-lead { display: block; color: var(--yellow); font-size: 13px; }
  .seal-text .seal-body { display: block; color: var(--white); font-size: 13px; }
  .seal-text .seal-big { display: block; color: var(--white); font-size: 19px; line-height: 1.05; }

  .call-bar { position: absolute; left: 0; top: 1140px; width: 708px; height: 60px; background: var(--yellow); display: flex; align-items: center; justify-content: center; color: var(--ink); font-weight: 800; font-size: 28px; letter-spacing: 0.3px; }
</style>
</head>
<body>
<main class="flyer">
  <header class="header">
    <div class="brand">Evergreen<br>Roofing</div>
    <svg class="warranty-panel" viewBox="0 0 708 160" aria-hidden="true">
      <polygon points="252,0 708,0 708,160 300,160 252,100" fill="var(--green)"/>
    </svg>
    <div class="warranty-up">UP TO</div>
    <div class="warranty-years">50 YEARS</div>
    <div class="warranty-sub">WARRANTY AVAILABLE</div>
  </header>

  <div class="hero-photo" role="img" aria-label="Photograph of a two-storey house with a new grey shingle roof and white garage door"></div>

  <svg class="divider" viewBox="0 0 708 120" aria-hidden="true">
    <polygon points="0,110 0,94 318,34 390,50 708,50 708,120" fill="var(--yellow)"/>
    <polygon points="0,120 0,104 318,46 390,62 708,62 708,120" fill="var(--white)"/>
    <polygon points="318,46 390,62 708,62 708,120 318,120" fill="var(--green)"/>
  </svg>

  <section class="lower">
    <div class="work-column">
      <div class="work-photo work-photo--roof" role="img" aria-label="Photograph of a pitched roof with new terracotta tiles and battens"></div>
      <div class="work-photo work-photo--fitter" role="img" aria-label="Photograph of a roofer cutting material on a roof"></div>
      <div class="ranks">
        <div class="rank">
          <svg class="rank-badge" viewBox="0 0 84 84" aria-hidden="true"><circle cx="42" cy="42" r="40" fill="var(--green-deep)" stroke="var(--yellow)" stroke-width="4"/></svg>
          <p class="rank-text"><strong>FLAT ROOFER</strong><br>in the UK Out Of 787<br>Registered Flat<br>Roofing Companies</p>
        </div>
        <div class="rank">
          <svg class="rank-badge" viewBox="0 0 84 84" aria-hidden="true"><circle cx="42" cy="42" r="40" fill="var(--green-deep)" stroke="var(--yellow)" stroke-width="4"/></svg>
          <p class="rank-text">Roofing Company in the UK out of<br>1976 registered Specialist Roofing<br>Companies both for<br><strong>COST, CUSTOMER SERVICE.</strong></p>
        </div>
      </div>
    </div>

    <div class="services">
      <h2 class="services-title">Repairs</h2>
      <ul class="service-list">
        <li><svg class="tick" viewBox="0 0 16 16" aria-hidden="true"><path d="M2 8 L6 12 L14 3" fill="none" stroke="var(--yellow)" stroke-width="2.5"/></svg>Roof Line Flat</li>
        <li><svg class="tick" viewBox="0 0 16 16" aria-hidden="true"><path d="M2 8 L6 12 L14 3" fill="none" stroke="var(--yellow)" stroke-width="2.5"/></svg>Roofs Pitched</li>
        <li><svg class="tick" viewBox="0 0 16 16" aria-hidden="true"><path d="M2 8 L6 12 L14 3" fill="none" stroke="var(--yellow)" stroke-width="2.5"/></svg>Roof Synthetic</li>
      </ul>
      <h2 class="about-title">About Us</h2>
      <p class="about-text">Lorem ipsum dolor sit amet, consectetur adipiscing elit, sed do eiusmod tempor incididunt ut labore et dolore magna aliqua. Ut enim ad minim veniam,</p>

      <div class="reviews">
        <h3 class="reviews-title">Customer feedback and review</h3>
        <div class="review">
          <p class="review-quote">“ Lorem ipsum dolor sit amet, consectetur adipiscing elit ”</p>
          <div class="review-foot"><span class="review-name">- Client's Name</span><span class="stars">★★★★★</span></div>
        </div>
        <div class="review">
          <p class="review-quote">“ Lorem ipsum dolor sit amet, consectetur adipiscing elit sed do eiusmod tempor ”</p>
          <div class="review-foot"><span class="review-name">- Client's Name</span><span class="stars">★★★★★</span></div>
        </div>
      </div>
    </div>
  </section>

  <svg class="seal" viewBox="0 0 150 150" aria-hidden="true">
    <circle cx="75" cy="75" r="72" fill="var(--white)"/>
    <circle cx="75" cy="75" r="67" fill="var(--yellow)"/>
    <circle cx="75" cy="75" r="60" fill="var(--charcoal)"/>
  </svg>
  <div class="seal-text">
    <span class="seal-lead">Guaranteed to</span>
    <span class="seal-body">Find &amp; fix a leak</span>
    <span class="seal-big">Approved</span>
    <span class="seal-body">Installers</span>
  </div>

  <footer class="call-bar">CALL 123-456-7890 FOR FREE ESTIMATION</footer>
</main>
</body>
</html>
```